Granite Ridge Holdings

I have a real estate investment business.

** I need editable vector files of the final design.

Industry/Entity Type

Real Estate

Contact Information for Business Card

I would like the card to be clear and direct with the company name and contact info. I would prefer not to have a design that is too busy (i.e., with excessive detail) in the business card.

Font styles to use
Sans Serif

Requirements
Must have
• My card must have the following information listed below:
• Company name: Grainite Ridge Holdings LLC
• My name: Daniel Vorsley
• Phone number: (555) 218-9067
• Email address: dtvorsley@mailbox-example.net
• Keywords: “Real Estate Investments”
Nice to have
• I would like to have a design that resembles the characteristics/uses of obsidian stone which resembles something related to strength and resilience. Perhaps something with sharp, sleek color transitions as well.

```html
<!DOCTYPE html>
<html lang="en">
<head>
<meta charset="utf-8">
<title>Granite Ridge Holdings – Business Card</title>
<link href="https://fonts.googleapis.com/css2?family=Lato:wght@400;700&display=swap" rel="stylesheet">
<style>
  :root {
    --backdrop: #3a3330;
    --card: #121212;
    --card-edge: #1c1c1c;
    --red: #d42026;
    --orange: #f39a1e;
    --silver: #c9c9c9;
    --grey: #a7a7a7;
    --rule: #2c2c2c;
    --white: #ededed;
  }
  * { margin: 0; padding: 0; box-sizing: border-box; }
  html, body {
    width: 1200px; height: 844px; overflow: hidden;
    background: var(--backdrop);
    font-family: "Lato", sans-serif;
  }
  .stage {
    position: relative; width: 1200px; height: 844px;
    display: flex; align-items: center; justify-content: center; gap: 40px;
  }
  .card {
    position: relative; width: 540px; height: 310px;
    background: var(--card);
    border: 1px solid var(--card-edge);
    box-shadow: 0 14px 30px rgba(0,0,0,.45);
  }

  /* Contact side */
  .brand-mark {
    position: absolute; left: 70px; top: 62px;
    width: 120px; height: 120px; border-radius: 50%;
    background: var(--red);
  }
  .brand-name {
    position: absolute; left: 30px; top: 198px; width: 200px;
    text-align: center; font-size: 13px; font-weight: 700;
    letter-spacing: .08em; color: var(--grey); text-transform: uppercase;
  }
  .divider {
    position: absolute; left: 262px; top: 60px;
    width: 1px; height: 110px; background: var(--rule);
  }
  .person {
    position: absolute; left: 290px; top: 72px;
    font-size: 17px; font-weight: 700; letter-spacing: .03em; text-transform: uppercase;
  }
  .person .first { color: var(--red); }
  .person .last { color: var(--orange); }
  .contacts { position: absolute; left: 290px; top: 116px; list-style: none; }
  .contacts li {
    display: flex; align-items: center; gap: 8px;
    font-size: 13px; color: var(--white); line-height: 22px;
  }
  .contacts svg { width: 11px; height: 11px; fill: var(--red); flex: none; }
  .tagline {
    position: absolute; left: 40px; bottom: 30px;
    font-size: 14px; letter-spacing: .04em; color: var(--grey); text-transform: uppercase;
  }

  /* Brand side */
  .card--brand { display: flex; flex-direction: column; align-items: center; justify-content: center; gap: 26px; }
  .card--brand .seal {
    width: 84px; height: 84px; border-radius: 50%; background: var(--silver);
  }
  .card--brand .company {
    font-size: 26px; font-weight: 400; letter-spacing: .06em;
    color: var(--silver); text-transform: uppercase;
  }
</style>
</head>
<body>
<main class="stage">
  <section class="card card--contact">
    <div class="brand-mark"></div>
    <div class="brand-name">Granite Ridge Holdings</div>
    <div class="divider"></div>
    <h1 class="person"><span class="first">Daniel</span> <span class="last">Vorsley</span></h1>
    <ul class="contacts">
      <li>
        <svg viewBox="0 0 12 12" aria-hidden="true"><path d="M2.2 1h2l1 2.6-1.3 1a6.5 6.5 0 0 0 3.5 3.5l1-1.3 2.6 1v2A1.2 1.2 0 0 1 9.8 11 8.8 8.8 0 0 1 1 2.2 1.2 1.2 0 0 1 2.2 1z"/></svg>
        (555) 218-9067
      </li>
      <li>
        <svg viewBox="0 0 12 12" aria-hidden="true"><path d="M1 2.5h10v7H1z M1.6 3l4.4 3.4L10.4 3" stroke="#121212" stroke-width=".9"/></svg>
        dtvorsley@mailbox-example.net
      </li>
    </ul>
    <p class="tagline">Real Estate Investments</p>
  </section>

  <section class="card card--brand">
    <div class="seal"></div>
    <div class="company">Granite Ridge Holdings</div>
  </section>
</main>
</body>
</html>
```